Produktdesign - Kosmetikprodukt
Zielgruppe
Damen ab 50
Aufgabenstellung
Ausgeschrieben wird ein ansprechendes und hochwertiges Produktdesign für eine neu einzuführende Creme zur Vergrößerung der weiblichen Brust.
Produktname: golden bloom
Verpackung: Weiße Tube mit Schraubverschluss
Zu verwendende Begriffe auf der Vorderseite:
- golden bloom als edler Schriftzug
- VOLUME effect
- DETOX effect
- FIRMING effect
Zu verwendende Informationen auf der Rückseite:
Mit Dreifach-Wirkkomplex....
VOLUME effect: stimuliert die Adipozytendifferenzierung, damit
funktionsfähige Adipozyten entstehen - positiver Effekt auf Volumen
DETOX effect: Kelarin aktiviert Proteasome 20S, die beschädigte
Zellen beseitigt und so die Zelltoxizität herabsetzt.
FIRMING effect: steigert die Dynamik der Fibrolasten um die Matrix
Wechselwirkungen wiederherzustellen.
- Barcode mit EAN: 4260913872145
- Inhalt: 50ml
- Made in germany
- Fendrik GmbH, Otto - Ranke - Str. 4, 54321 Kaltenbrück

```html
<!DOCTYPE html>
<html lang="de">
<head>
<meta charset="utf-8">
<title>Golden Bloom – Tubendesign</title>
<link rel="stylesheet" href="https://fonts.googleapis.com/css2?family=Tinos:wght@400;700&display=swap">
<style>
  :root {
    --page: #ffffff;
    --tube-white: #ffffff;
    --tube-shade: #cfcfcf;
    --tube-edge: #9a9a9a;
    --cap-light: #e9e9e9;
    --cap-mid: #8c8c8c;
    --cap-dark: #1e1e1e;
    --ink: #111111;
    --silhouette: #d9d9d9;
  }
  html, body {
    margin: 0;
    padding: 0;
    width: 1200px;
    height: 1158px;
    overflow: hidden;
    background: var(--page);
  }
  .packaging {
    display: block;
    width: 1200px;
    height: 1158px;
    font-family: "Tinos", "Times New Roman", serif;
  }
  .brand-name { font-size: 112px; fill: var(--ink); }
  .claim { font-size: 22px; fill: var(--ink); }
  .back-heading { font-size: 21px; font-weight: 700; fill: var(--ink); }
  .back-effect { font-size: 20px; font-weight: 700; fill: var(--ink); }
  .back-copy { font-size: 18px; fill: var(--ink); }
  .back-info { font-size: 18px; fill: var(--ink); }
</style>
</head>
<body>
<svg class="packaging" viewBox="0 0 1200 1158" xmlns="http://www.w3.org/2000/svg">
  <defs>
    <linearGradient id="tube-body" x1="0" x2="1" y1="0" y2="0">
      <stop offset="0" stop-color="var(--tube-shade)"/>
      <stop offset="0.12" stop-color="var(--tube-white)"/>
      <stop offset="0.85" stop-color="var(--tube-white)"/>
      <stop offset="1" stop-color="var(--tube-shade)"/>
    </linearGradient>
    <linearGradient id="cap-metal" x1="0" x2="1" y1="0" y2="0">
      <stop offset="0" stop-color="var(--cap-dark)"/>
      <stop offset="0.3" stop-color="var(--cap-mid)"/>
      <stop offset="0.5" stop-color="var(--cap-light)"/>
      <stop offset="0.75" stop-color="var(--cap-mid)"/>
      <stop offset="1" stop-color="var(--cap-dark)"/>
    </linearGradient>
    <linearGradient id="cap-collar" x1="0" x2="0" y1="0" y2="1">
      <stop offset="0" stop-color="var(--tube-white)"/>
      <stop offset="1" stop-color="var(--tube-shade)"/>
    </linearGradient>
    <linearGradient id="silhouette-fill" x1="0" x2="1" y1="0" y2="0">
      <stop offset="0" stop-color="var(--tube-white)"/>
      <stop offset="0.5" stop-color="var(--silhouette)"/>
      <stop offset="1" stop-color="var(--tube-white)"/>
    </linearGradient>
  </defs>

  <!-- Front tube -->
  <g class="tube tube-front">
    <path class="tube-body" d="M74 14 L554 14 L470 960 L150 960 Z" fill="url(#tube-body)" stroke="var(--tube-edge)" stroke-width="2"/>
    <line class="tube-crimp" x1="74" y1="30" x2="554" y2="30" stroke="var(--tube-shade)" stroke-width="2"/>
    <rect class="cap-collar" x="150" y="960" width="320" height="50" fill="url(#cap-collar)" stroke="var(--tube-edge)" stroke-width="2"/>
    <rect class="cap-metal" x="150" y="1010" width="320" height="108" rx="6" fill="url(#cap-metal)"/>

    <rect class="silhouette" role="img" aria-label="Dezente Silhouette eines weiblichen Oberkörpers" x="262" y="60" width="108" height="560" rx="50" fill="url(#silhouette-fill)" opacity="0.7"/>

    <text class="brand-name" x="255" y="720" transform="rotate(-90 255 720)">Golden Bloom</text>

    <text class="claim" x="222" y="742">VOLUME effect</text>
    <text class="claim" x="222" y="798">DETOX effect</text>
    <text class="claim" x="222" y="852">FIRMING effect</text>
  </g>

  <!-- Back tube -->
  <g class="tube tube-back">
    <path class="tube-body" d="M645 14 L1122 14 L1047 960 L716 960 Z" fill="url(#tube-body)" stroke="var(--tube-edge)" stroke-width="2"/>
    <line class="tube-crimp" x1="645" y1="30" x2="1122" y2="30" stroke="var(--tube-shade)" stroke-width="2"/>
    <rect class="cap-collar" x="716" y="960" width="331" height="50" fill="url(#cap-collar)" stroke="var(--tube-edge)" stroke-width="2"/>
    <rect class="cap-metal" x="716" y="1010" width="331" height="108" rx="6" fill="url(#cap-metal)"/>

    <g class="ingredient-copy" text-anchor="middle">
      <text class="back-heading" x="887" y="150">Mit Dreifach-Wirkkomplex</text>

      <text class="back-effect" x="887" y="200">VOLUME effect</text>
      <text class="back-copy" x="887" y="227">stimuliert die Adipozytendifferenzierung</text>
      <text class="back-copy" x="887" y="253">damit funktionsfähige</text>
      <text class="back-copy" x="887" y="279">Adipozyten entstehen -</text>
      <text class="back-copy" x="887" y="305">positiver Effekt auf Volumen</text>

      <text class="back-effect" x="887" y="340">DETOX effect</text>
      <text class="back-copy" x="887" y="367">Kelarin aktiviert Proteasome 20S</text>
      <text class="back-copy" x="887" y="393">die beschädigte Zellen beseitigt und die</text>
      <text class="back-copy" x="887" y="419">Zelltoxizität herabsetzt</text>

      <text class="back-effect" x="887" y="478">FIRMING effect</text>
      <text class="back-copy" x="887" y="505">steigert die Dynamik der Fibrolasten</text>
      <text class="back-copy" x="887" y="531">um die Matrix Wechselwirkungen</text>
      <text class="back-copy" x="887" y="557">wiederherzustellen</text>
    </g>

    <g class="product-info">
      <text class="back-info" x="776" y="700">Inhalt: 50ml</text>
      <text class="back-info" x="776" y="734">Made in Germany</text>
      <text class="back-info" x="776" y="900">Fendrik GmbH, Otto - Ranke -</text>
      <text class="back-info" x="776" y="928">Str. 4, 54321 Kaltenbrück</text>
    </g>
  </g>
</svg>
</body>
</html>
```